Gold and Ember med spa needs an awesome eye catching billboard ad

We need a billboard ad design for a Med Spa with location sin Brentmoor and Windermere FL A medical spa where the beauty of nature meets the power of science to treat the whole person, mind, body and soul.

Tallory Brightway Med Spa is a medical spa where the beauty of nature meets the power of science to create gorgeous, youthful looking skin. Located in Brentmoor, Florida, but also serving Four Corners, Celebration, and Windermere, Florida, the talented professional team brings decades of experience in world-class skin care to provide holistic, science-backed aesthetic services and health coaching.

Industry/Entity Type

Spa

Colors
fbee3e
fece3e
eea4c8
e667a6
fbee3d

Requirements
Must have
• Locations in Brentmoor and Oak Hollow
Phone 407-555-0193
website www.goldandemberspa-example.com

Boards for each:
Aesthetic Treatments
Cosmetic Injectables
Lumiva facial
add color vs too many earthtones, to catch the eye perhaps using yellow, something that catches the eye and stands out from the normal everyday
Thank you!!!!
Nice to have
• Boards for each:
Aesthetic Treatments
Cosmetic Injectables
Lumiva facial
add color vs too many earthtones, to catch the eye
photos that match services,
Thank you!!!!

```html
<!DOCTYPE html>
<html lang="en">
<head>
<meta charset="utf-8">
<title>Lumiva Facial Billboard – Tallory Brightway Med Spa</title>
<link href="https://fonts.googleapis.com/css2?family=Cinzel:wght@700&family=Montserrat:wght@500;600&display=swap" rel="stylesheet">
<style>
  :root {
    --stage: #e9ecef;
    --board: #fbfbfb;
    --pink: #e667a6;
    --teal: #5fb7b2;
    --ink: #4a4a4a;
    --water-light: #e6f1f4;
    --water-mid: #b9d3dc;
    --skin: #e8c9b8;
  }
  * { margin: 0; padding: 0; box-sizing: border-box; }
  html, body { width: 1200px; height: 1010px; overflow: hidden; }
  body {
    background: var(--stage);
    position: relative;
    font-family: "Montserrat", sans-serif;
  }
  .billboard {
    position: absolute;
    left: 0;
    top: 355px;
    width: 1200px;
    height: 300px;
    background: var(--board);
    overflow: hidden;
  }
  .hero-photo {
    position: absolute;
    left: 0;
    top: 0;
    width: 440px;
    height: 300px;
    background:
      radial-gradient(ellipse 90px 120px at 300px 120px, var(--skin) 0%, rgba(232,201,184,0) 100%),
      linear-gradient(100deg, var(--water-mid) 0%, var(--water-light) 55%, rgba(251,251,251,0) 100%);
  }
  .headline {
    position: absolute;
    left: 405px;
    top: 62px;
    font-family: "Cinzel", serif;
    font-weight: 700;
    font-size: 52px;
    line-height: 1;
    color: var(--pink);
    letter-spacing: 0.5px;
    white-space: nowrap;
  }
  .locations {
    position: absolute;
    left: 402px;
    top: 133px;
    width: 362px;
    height: 30px;
    background: var(--teal);
    color: var(--ink);
    font-weight: 500;
    font-size: 18.5px;
    line-height: 30px;
    padding-left: 18px;
    white-space: nowrap;
  }
  .phone {
    position: absolute;
    left: 403px;
    top: 190px;
    font-weight: 600;
    font-size: 34px;
    line-height: 1;
    color: var(--ink);
    white-space: nowrap;
  }
  .website {
    position: absolute;
    left: 404px;
    top: 232px;
    font-weight: 600;
    font-size: 15px;
    line-height: 1;
    letter-spacing: 1.1px;
    color: var(--ink);
    white-space: nowrap;
  }
  .brand {
    position: absolute;
    left: 785px;
    top: 172px;
    display: flex;
    align-items: center;
    gap: 18px;
  }
  .brand-dot {
    width: 72px;
    height: 72px;
    border-radius: 50%;
    background: var(--teal);
    flex: none;
  }
  .brand-name {
    font-weight: 500;
    font-size: 25px;
    line-height: 1.3;
    letter-spacing: 3px;
    color: var(--pink);
    text-transform: uppercase;
    white-space: nowrap;
  }
</style>
</head>
<body>
  <section class="billboard">
    <div class="hero-photo" role="img" aria-label="Photo of a woman's face surrounded by a splash of clear water"></div>
    <h1 class="headline">Lumiva facial</h1>
    <p class="locations">BRENTMOOR AND OAK HOLLOW</p>
    <p class="phone">407-555-0193</p>
    <p class="website">WWW.GOLDANDEMBERSPA-EXAMPLE.COM</p>
    <div class="brand">
      <span class="brand-dot"></span>
      <p class="brand-name">Tallory<br>Brightway<br>Med Spa</p>
    </div>
  </section>
</body>
</html>
```